Business Cards

Need business card design that I can update for new employees and details. Needs to incorporate our logo, be bright and fun (in line with tourism and holidays)
Would like a Map of Western Australia on the front with locations all the caravan parks we own (just purchased Tom Price so please include that as well as others listed on our website).
Target Market(s)
Famillies
Contact Information for Business Card
5 Cards -
Mark Pettigrew (Director) e: pettigrew@bluewattle.com.au p: 0462 318 904
Lucy Pettigrew (Director) e: pettigrew@bluewattle.com.au p: 0455 896 320
Peter Halvorsen (General Manager) e: halvorsen@bluewattle.com.au p: 0471 552 648
Mina Halvorsen (General Manager) e: halvorsen@bluewattle.com.au p: 0471 552 649
Neil Whitcombe (Training and Operations Manager) - e: whitcombe@bluewattle.com.au p:0427 160 493
Colors
Designer to choose colors to be used in the design.
Look and feel
Each slider illustrates characteristics of the customer's brand and the style your logo design should communicate.

```html
<!DOCTYPE html>
<html lang="en">
<head>
<meta charset="utf-8">
<title>Bluewattle Tourist Parks – Business Cards</title>
<link rel="stylesheet" href="https://fonts.googleapis.com/css2?family=Cinzel:wght@400&family=Open+Sans:wght@400&display=swap">
<style>
  :root {
    --backdrop: #e9e9e9;
    --card-white: #fbfbfb;
    --brand-teal: #42c1cc;
    --ink-grey: #4a4a4a;
    --ink-soft: #6b6b6b;
    --card-shadow: rgba(0, 0, 0, 0.14);
  }
  * { box-sizing: border-box; margin: 0; padding: 0; }
  html, body {
    width: 1200px;
    height: 900px;
    overflow: hidden;
    background: var(--backdrop);
  }
  .sheet {
    position: relative;
    width: 1200px;
    height: 900px;
    display: flex;
    align-items: center;
    justify-content: center;
    gap: 70px;
  }
  .card {
    position: relative;
    width: 500px;
    height: 286px;
    border-radius: 3px;
    box-shadow: 0 14px 30px var(--card-shadow);
  }
  .card--front { background: var(--card-white); }
  .card--back { background: var(--brand-teal); }

  .holder {
    position: absolute;
    left: 34px;
    top: 32px;
  }
  .holder__name {
    font-family: "Cinzel", serif;
    font-size: 17px;
    letter-spacing: 0.5px;
    color: var(--brand-teal);
  }
  .holder__role {
    font-family: "Open Sans", sans-serif;
    font-size: 10px;
    color: var(--ink-soft);
    margin-top: 2px;
  }

  .contact {
    position: absolute;
    left: 34px;
    top: 118px;
    list-style: none;
    font-family: "Open Sans", sans-serif;
    font-size: 11px;
    color: var(--ink-grey);
  }
  .contact__item {
    display: flex;
    align-items: center;
    gap: 7px;
    margin-bottom: 6px;
  }
  .contact__icon { width: 14px; height: 14px; flex: none; }

  .brand {
    position: absolute;
    display: flex;
    align-items: center;
    gap: 12px;
    font-family: "Cinzel", serif;
    font-weight: 400;
  }
  .brand--front {
    right: 34px;
    top: 118px;
    color: var(--ink-grey);
  }
  .brand--back {
    left: 50%;
    top: 50%;
    transform: translate(-50%, -50%);
    color: #ffffff;
  }
  .brand__mark {
    width: 46px;
    height: 46px;
    flex: none;
  }
  .brand--front .brand__mark { background: var(--brand-teal); }
  .brand--back .brand__mark { background: #ffffff; }
  .brand__name {
    font-size: 24px;
    letter-spacing: 3px;
    line-height: 1.1;
  }
  .brand__tag {
    display: block;
    font-size: 11px;
    letter-spacing: 4px;
    text-align: center;
  }
</style>
</head>
<body>
<main class="sheet">
  <section class="card card--front">
    <div class="holder">
      <p class="holder__name">MARK PETTIGREW</p>
      <p class="holder__role">Director</p>
    </div>
    <ul class="contact">
      <li class="contact__item">
        <svg class="contact__icon" viewBox="0 0 14 14" aria-hidden="true">
          <rect width="14" height="14" fill="#42c1cc"/>
          <path d="M4 3.2c.5-.3 1-.2 1.2.3l.6 1.3c.1.3 0 .6-.2.8l-.5.4c.4.9 1.1 1.6 2 2l.4-.5c.2-.2.5-.3.8-.2l1.3.6c.5.2.6.7.3 1.2-.5.8-1.4 1.1-2.3.7C5.8 9 5 8.2 4.2 6.6c-.4-.9-.9-2.6-.2-3.4z" fill="#fff"/>
        </svg>
        <span>0462 318 904</span>
      </li>
      <li class="contact__item">
        <svg class="contact__icon" viewBox="0 0 14 14" aria-hidden="true">
          <rect width="14" height="14" fill="#42c1cc"/>
          <rect x="3" y="4" width="8" height="6" fill="none" stroke="#fff" stroke-width="1"/>
          <path d="M3 4l4 3.2L11 4" fill="none" stroke="#fff" stroke-width="1"/>
        </svg>
        <span>pettigrew@bluewattle.com.au</span>
      </li>
    </ul>
    <div class="brand brand--front">
      <div>
        <span class="brand__name">BLUEWATTLE</span>
        <span class="brand__tag">TOURIST PARKS</span>
      </div>
      <span class="brand__mark"></span>
    </div>
  </section>

  <section class="card card--back">
    <div class="brand brand--back">
      <div>
        <span class="brand__name">BLUEWATTLE</span>
        <span class="brand__tag">TOURIST PARKS</span>
      </div>
      <span class="brand__mark"></span>
    </div>
  </section>
</main>
</body>
</html>
```